Restaurant Bar website in Oakland

Landing page that looks good on mobile and home. Easy to make changes to SEO and Menu page .
Might link with online ordering through the point of sale provider or not. Either way we want to be able to upload menus.
No forms need. Just landing page, about page with a paragraph and a few photos, address, hours and a mailto info@
A press page and an faq

Target Market(s)

Customers

Coding

Coded - Design and coding required

Number of Pages Required

4 page

Colors
00a990
ffc214

Requirements
Must have
• Simple to scroll
SEO
Simple to add menus
Our logo

```html
<!DOCTYPE html>
<html lang="en">
<head>
<meta charset="utf-8">
<title>Marlo's Restaurant Bar</title>
<link href="https://fonts.googleapis.com/css2?family=Montserrat:wght@500;600;700;800&family=Open+Sans:wght@400;600;700&display=swap" rel="stylesheet">
<style>
:root{
  --teal:#00a990;
  --yellow:#ffc214;
  --gold:#a0782a;
  --dark:#1f1f1f;
  --text:#555;
  --muted:#888;
  --light:#f4f4f4;
  --white:#fff;
  --line:rgba(255,255,255,.45);
}
*{box-sizing:border-box;margin:0;padding:0}
html,body{width:1200px;height:5128px;overflow:hidden}
body{font-family:"Open Sans",Arial,sans-serif;color:var(--text);background:var(--white)}
h1,h2,h3,.label,.btn,.nav a,.brand{font-family:"Montserrat",Arial,sans-serif}
figure{margin:0}

.topbar{height:28px;background:var(--teal);color:var(--white);font-size:13px;display:flex;justify-content:center;align-items:center;gap:28px}
.topbar span{display:flex;align-items:center;gap:7px}

.nav{height:104px;position:relative;display:flex;align-items:center;padding:0 112px;justify-content:space-between}
.nav ul{list-style:none;display:flex;gap:44px}
.nav a{text-decoration:none;color:var(--dark);font-size:14px;font-weight:600;text-transform:uppercase}
.nav a.active{color:var(--yellow)}
.brand-tab{position:absolute;left:50%;top:0;transform:translateX(-50%);width:260px;height:170px;background:var(--white);border-radius:0 0 130px 130px;z-index:3;display:flex;align-items:center;justify-content:center;gap:10px;padding-bottom:20px}
.brand{font-size:34px;font-weight:800;color:var(--gold);letter-spacing:1px}
.brand-dot{width:14px;height:14px;border-radius:50%;background:var(--gold)}

.hero{height:556px;position:relative;
  background:
    radial-gradient(ellipse 140px 200px at 1010px 210px,rgba(246,178,40,.9),rgba(246,178,40,0) 75%),
    radial-gradient(ellipse 260px 150px at 700px 330px,rgba(120,55,35,.95),rgba(120,55,35,0) 80%),
    radial-gradient(ellipse 360px 90px at 560px 470px,rgba(210,150,70,.8),rgba(210,150,70,0) 80%),
    linear-gradient(180deg,#8a8078 0%,#b7aea4 40%,#6e5038 78%,#3d2618 100%)}
.hero-copy{position:absolute;left:112px;top:128px;color:var(--white)}
.hero h1{font-size:46px;font-weight:800;line-height:1.15;text-transform:uppercase;color:var(--white)}
.hero p{margin:14px 0 34px;font-size:19px;font-weight:600}
.btn{display:inline-block;background:var(--yellow);color:var(--white);font-weight:700;font-size:15px;padding:20px 28px;border-radius:6px;text-transform:uppercase;text-decoration:none}

.label{color:var(--teal);font-size:20px;font-weight:600;text-transform:uppercase}
h2{font-size:46px;font-weight:800;color:var(--dark);text-transform:uppercase;line-height:1.1}

.about{height:532px;display:flex;align-items:center;gap:56px;padding:0 112px}
.about-photo{width:424px;height:380px;border-radius:10px 10px 60px 10px;
  background:
    radial-gradient(ellipse 70px 110px at 250px 140px,rgba(30,40,45,.95),rgba(30,40,45,0) 85%),
    radial-gradient(ellipse 120px 150px at 250px 290px,rgba(200,150,120,.9),rgba(200,150,120,0) 80%),
    linear-gradient(135deg,#efefef,#bdbdbd 55%,#7a7a7a)}
.about-copy{width:500px}
.about-copy h2{margin:6px 0 18px}
.about-copy p{font-size:15px;line-height:1.75;margin-bottom:30px}

.menu{height:1428px;background:var(--light);padding-top:70px;text-align:center}
.menu h2{margin-top:4px}
.grid{width:976px;margin:48px auto 0;display:flex;flex-direction:column;gap:10px}
.row{display:flex;gap:8px;height:348px}
.dish{position:relative;border-radius:4px;overflow:hidden}
.dish::after{content:"";position:absolute;inset:auto 0 0 0;height:90px;background:linear-gradient(0deg,rgba(0,0,0,.55),rgba(0,0,0,0))}
.dish figcaption{position:absolute;left:20px;right:20px;bottom:16px;display:flex;justify-content:space-between;color:var(--white);font-weight:700;font-size:17px;z-index:1}
.d1{background:radial-gradient(ellipse 170px 110px at 50% 55%,#d9b37c,rgba(217,179,124,0) 85%),linear-gradient(160deg,#5b3a24,#2a1a10)}
.d2{background:radial-gradient(ellipse 200px 130px at 38% 45%,#8e3a22,rgba(142,58,34,0) 85%),radial-gradient(ellipse 170px 140px at 80% 65%,#f1b63a,rgba(241,182,58,0) 85%),linear-gradient(160deg,#4a2a1a,#6e4a30)}
.d3{background:radial-gradient(ellipse 130px 100px at 30% 45%,#b8532e,rgba(184,83,46,0) 85%),radial-gradient(ellipse 130px 100px at 72% 60%,#9a4a2a,rgba(154,74,42,0) 85%),linear-gradient(160deg,#3a3a30,#1f1d18)}
.d4{background:radial-gradient(ellipse 170px 120px at 50% 45%,#e2a54c,rgba(226,165,76,0) 85%),linear-gradient(170deg,#2b2622,#6a5540)}
.d5{background:radial-gradient(ellipse 110px 120px at 30% 55%,#b5773a,rgba(181,119,58,0) 85%),radial-gradient(ellipse 110px 120px at 62% 50%,#a86a32,rgba(168,106,50,0) 85%),linear-gradient(160deg,#5c4634,#241a14)}
.d6{background:radial-gradient(ellipse 150px 110px at 50% 55%,#c98a5a,rgba(201,138,90,0) 85%),linear-gradient(160deg,#3e2c40,#1d1620)}
.menu .btn{margin-top:44px}

.press{height:656px;padding-top:72px;text-align:center}
.press h2{margin-top:4px}
.cards{width:976px;margin:44px auto 0;display:flex;gap:23px;text-align:left}
.card{width:310px}
.card-photo{height:232px}
.c1{background:radial-gradient(ellipse 160px 90px at 50% 75%,#c9862e,rgba(201,134,46,0) 85%),linear-gradient(160deg,#6a2a1a,#2a140c)}
.c2{background:radial-gradient(ellipse 120px 110px at 50% 60%,#d8a060,rgba(216,160,96,0) 85%),linear-gradient(160deg,#e8e2da,#a89888)}
.c3{background:radial-gradient(ellipse 160px 110px at 70% 30%,#f4dfa0,rgba(244,223,160,0) 85%),linear-gradient(170deg,#c7a26a,#4a3a2a)}
.card h3{font-size:20px;font-weight:700;color:var(--dark);margin:24px 0 8px;white-space:nowrap}
.meta{font-size:12px;display:flex;gap:16px;margin-bottom:10px;color:var(--muted)}
.meta span{display:flex;align-items:center;gap:5px}
.meta svg{width:12px;height:12px}
.card p{font-size:13px;line-height:1.65}

.faq{height:684px;background:var(--teal);color:var(--white);padding-top:56px;text-align:center}
.faq .label{color:var(--white);font-size:18px}
.faq h2{color:var(--white);margin-top:4px;font-size:44px;font-weight:700}
.faq-list{width:800px;margin:36px auto 0;text-align:left}
.faq-item{border-bottom:1px solid var(--line);padding:18px 0;font-size:17px;font-weight:600;display:flex;justify-content:space-between;flex-wrap:wrap}
.faq-item .answer{width:100%;font-size:14px;font-weight:400;line-height:1.7;margin-top:12px}
.sign{font-size:22px;font-weight:400;line-height:1}

.visit{height:800px;position:relative;
  background:
    radial-gradient(ellipse 220px 160px at 150px 620px,rgba(190,130,70,.8),rgba(190,130,70,0) 85%),
    radial-gradient(ellipse 200px 160px at 1060px 560px,rgba(220,200,170,.75),rgba(220,200,170,0) 85%),
    radial-gradient(ellipse 260px 140px at 1000px 120px,rgba(110,140,60,.7),rgba(110,140,60,0) 85%),
    linear-gradient(120deg,#1d2b1f,#4a3a28 45%,#2b2119 100%)}
.visit-box{position:absolute;left:280px;top:64px;width:640px;height:648px;background:rgba(255,255,255,.82);text-align:center;padding-top:40px;color:#333}
.visit-box h3{font-size:32px;font-weight:700;text-transform:uppercase;color:var(--dark);margin-bottom:14px}
.visit-box h3.hours{margin-top:30px}
.visit-box p{font-size:16px;line-height:1.6}
.ic{width:36px;height:36px;margin:16px auto 8px;display:block}

.footer{height:340px;text-align:center;padding-top:50px}
.footer .brand-row{display:flex;justify-content:center;align-items:center;gap:10px;height:110px}
.footer ul{list-style:none;display:flex;justify-content:center;gap:10px;font-size:15px;margin-top:20px}
.footer small{display:block;font-size:14px;margin-top:12px}
.social{display:flex;justify-content:center;gap:14px;margin-top:18px}
.social span{width:36px;height:36px;border:2px solid var(--gold);border-radius:50%;display:flex;align-items:center;justify-content:center}
.social svg{width:16px;height:16px}
</style>
</head>
<body>
<div class="topbar">
  <span><svg width="14" height="14" viewBox="0 0 24 24"><rect x="2" y="5" width="20" height="14" fill="#fff"/><path d="M2 5l10 8 10-8" stroke="#00a990" stroke-width="2" fill="none"/></svg>info@marlos.example</span>
  <span><svg width="14" height="14" viewBox="0 0 24 24" fill="#fff"><path d="M6 2l4 5-2 3a12 12 0 006 6l3-2 5 4-3 4C10 22 2 14 2 5z"/></svg>1 555 010 0199</span>
</div>
<header class="nav">
  <ul>
    <li><a class="active" href="#">Home</a></li>
    <li><a href="#">About</a></li>
    <li><a href="#">Menu</a></li>
  </ul>
  <div class="brand-tab"><span class="brand-dot"></span><span class="brand">MARLO'S</span></div>
  <ul>
    <li><a href="#">Press</a></li>
    <li><a href="#">FAQ</a></li>
    <li><a href="#">Contact Us</a></li>
  </ul>
</header>
<section class="hero" role="img" aria-label="Burger with fries, a dip and a glass of beer on a wooden board">
  <div class="hero-copy">
    <h1>Marlo's<br>Restaurant Bar</h1>
    <p>Nemo enim ipsam voluptatem quia volupt</p>
    <a class="btn" href="#">Order now!</a>
  </div>
</section>
<section class="about">
  <div class="about-photo" role="img" aria-label="Hand holding a phone showing the online ordering page"></div>
  <div class="about-copy">
    <div class="label">About</div>
    <h2>Welcome to<br>Marlo's</h2>
    <p>Lorem ipsum dolor sit amet, consectetur adipiscing elit, sed do eiusmod tempor incididunt ut labore et dolore magna aliqua. Ut enim ad minim veniam, quis nostrud exercitation ullamco laboris nisi ut aliquip ex ea commodo consequat. Duis aute irure dolor.</p>
    <a class="btn" href="#">Read more</a>
  </div>
</section>
<section class="menu">
  <div class="label">Menu</div>
  <h2>Our Favorites</h2>
  <div class="grid">
    <div class="row">
      <figure class="dish d1" style="width:388px" role="img" aria-label="Club sandwich on a board"><figcaption><span>Finibus Bonoruet Malorum</span><span>$34</span></figcaption></figure>
      <figure class="dish d2" style="width:580px" role="img" aria-label="Steak with fries"><figcaption><span>Finibus Bonoruet Malorum</span><span>$28</span></figcaption></figure>
    </div>
    <div class="row">
      <figure class="dish d3" style="width:480px" role="img" aria-label="Shared plates of appetizers"><figcaption><span>Finibus Bonoruet Malorum</span><span>$28</span></figcaption></figure>
      <figure class="dish d4" style="width:488px" role="img" aria-label="Cheeseburger"><figcaption><span>Finibus Bonoruet Malorum</span><span>$28</span></figcaption></figure>
    </div>
    <div class="row">
      <figure class="dish d5" style="width:576px" role="img" aria-label="Two burgers on a table"><figcaption><span>Finibus Bonoruet Malorum</span><span>$28</span></figcaption></figure>
      <figure class="dish d6" style="width:392px" role="img" aria-label="Wraps on a plate"><figcaption><span>Finibus Bonoruet Malorum</span><span>$34</span></figcaption></figure>
    </div>
  </div>
  <a class="btn" href="#">View more</a>
</section>
<section class="press">
  <div class="label">Press</div>
  <h2>Latest Blog</h2>
  <div class="cards">
    <article class="card"><div class="card-photo c1" role="img" aria-label="Friends dining together"></div><h3>Ut enim ad minima venia</h3><div class="meta"><span><svg viewBox="0 0 12 12"><rect x="1" y="2" width="10" height="9" rx="1" fill="#ffc214"/></svg>2/8/2021</span><span><svg viewBox="0 0 12 12"><circle cx="6" cy="4" r="2.5" fill="#ffc214"/><path d="M1.5 11a4.5 4.5 0 019 0z" fill="#ffc214"/></svg>Admin</span></div><p>Nemo enim ipsam voluptatem quia volu ptas sit aspernatur aut odit aut fugit, sed quia consequ mag.</p></article>
    <article class="card"><div class="card-photo c2" role="img" aria-label="Burger held over a plate"></div><h3>Ut enim ad minima venia</h3><div class="meta"><span><svg viewBox="0 0 12 12"><rect x="1" y="2" width="10" height="9" rx="1" fill="#ffc214"/></svg>2/8/2021</span><span><svg viewBox="0 0 12 12"><circle cx="6" cy="4" r="2.5" fill="#ffc214"/><path d="M1.5 11a4.5 4.5 0 019 0z" fill="#ffc214"/></svg>Admin</span></div><p>Nemo enim ipsam voluptatem quia volu ptas sit aspernatur aut odit aut fugit, sed quia consequ mag.</p></article>
    <article class="card"><div class="card-photo c3" role="img" aria-label="Glasses on a restaurant table at sunset"></div><h3>Ut enim ad minima venia</h3><div class="meta"><span><svg viewBox="0 0 12 12"><rect x="1" y="2" width="10" height="9" rx="1" fill="#ffc214"/></svg>2/8/2021</span><span><svg viewBox="0 0 12 12"><circle cx="6" cy="4" r="2.5" fill="#ffc214"/><path d="M1.5 11a4.5 4.5 0 019 0z" fill="#ffc214"/></svg>Admin</span></div><p>Nemo enim ipsam voluptatem quia volu ptas sit aspernatur aut odit aut fugit, sed quia consequ mag.</p></article>
  </div>
</section>
<section class="faq">
  <div class="label">Q&amp;A</div>
  <h2>Frequently Asked Questions</h2>
  <div class="faq-list">
    <div class="faq-item"><span>Sed ut perspiciatis unde o sit voluptatem accusa?</span><span class="sign">&minus;</span><p class="answer">Nemo enim ipsam voluptatem quia voluptas sit aspernatur aut odit aut fugit, sed quia conse quuntur magni dolores eos qui ratione voluptatem sequi nesciunt. Neque porro quisquam est, qui dolorem ipsum quia dolor sit amet, consectetur, adipisc.</p></div>
    <div class="faq-item"><span>Sed ut perspiciatis unde o sit voluptatem accusa?</span><span class="sign">+</span></div>
    <div class="faq-item"><span>Sed ut perspiciatis unde o sit voluptatem accusa?</span><span class="sign">+</span></div>
    <div class="faq-item"><span>Sed ut perspiciatis unde o sit voluptatem accusa?</span><span class="sign">+</span></div>
    <div class="faq-item"><span>Sed ut perspiciatis unde o sit voluptatem accusa?</span><span class="sign">+</span></div>
  </div>
</section>
<section class="visit" role="img" aria-label="Guests sharing dinner at a busy restaurant table">
  <div class="visit-box">
    <h3>Location</h3>
    <svg class="ic" viewBox="0 0 24 24"><circle cx="12" cy="12" r="12" fill="#ffc214"/><path d="M12 5a4 4 0 00-4 4c0 3 4 9 4 9s4-6 4-9a4 4 0 00-4-4z" fill="#fff"/></svg>
    <p>4200 Harbor Lane, Oakland,<br>CA 94600</p>
    <svg class="ic" viewBox="0 0 24 24"><circle cx="12" cy="12" r="12" fill="#ffc214"/><path d="M8 6l2 3-1 2a7 7 0 004 4l2-1 3 2-2 2C11 18 6 13 6 8z" fill="#fff"/></svg>
    <p>1 555 010 0199</p>
    <svg class="ic" viewBox="0 0 24 24"><circle cx="12" cy="12" r="12" fill="#ffc214"/><rect x="6" y="8" width="12" height="8" fill="#fff"/><path d="M6 8l6 5 6-5" stroke="#ffc214" fill="none"/></svg>
    <p>info@marlos.example</p>
    <h3 class="hours">Hours</h3>
    <svg class="ic" viewBox="0 0 24 24"><circle cx="12" cy="12" r="12" fill="#ffc214"/><circle cx="12" cy="12" r="6" fill="none" stroke="#fff" stroke-width="2"/><path d="M12 9v3h2" stroke="#fff" stroke-width="2" fill="none"/></svg>
    <p>Monday – Thursday: 8PM-9PM<br>Friday, Saturday: 4PM-10PM<br>Sunday: CLOSED</p>
  </div>
</section>
<footer class="footer">
  <div class="brand-row"><span class="brand-dot"></span><span class="brand">MARLO'S</span></div>
  <ul><li>Home</li><li>|</li><li>About</li><li>|</li><li>Menu</li><li>|</li><li>Press</li><li>|</li><li>FAQ</li><li>|</li><li>Contact Us</li></ul>
  <small>Marlo's © 2021. All right reserved.</small>
  <div class="social">
    <span aria-label="Email"><svg viewBox="0 0 24 24"><rect x="3" y="6" width="18" height="12" fill="none" stroke="#a0782a" stroke-width="2"/><path d="M3 6l9 7 9-7" stroke="#a0782a" stroke-width="2" fill="none"/></svg></span>
    <span aria-label="Phone"><svg viewBox="0 0 24 24"><path d="M6 2l4 5-2 3a12 12 0 006 6l3-2 5 4-3 4C10 22 2 14 2 5z" fill="#a0782a"/></svg></span>
    <span aria-label="Location"><svg viewBox="0 0 24 24"><path d="M12 2a7 7 0 00-7 7c0 5 7 13 7 13s7-8 7-13a7 7 0 00-7-7z" fill="#a0782a"/><circle cx="12" cy="9" r="2.5" fill="#fff"/></svg></span>
  </div>
</footer>
</body>
</html>
```